tilebaron.org needs a cool website!

I need a website designed for a commercial flooring maintenance company based in Texas. We will be providing services like carpet shampooing, burnishing, resurfacing and power washing. It needs to be cool and trendy.

I’ll need 10-20 pages. I need help deciding on the style and color palette. We will need great stock pictures of different flooring types and you will need to photo shop our logo on imaginary cars or storefronts.

Please have similar experience and an open mind. I’m looking for a partnership and someone to turn to for future projects and upkeep.

The domain is currently hosted on Wix. You will need the ability to develop and code it there.
Updates

Target Market(s)

Commercial businesses and properties

Industry/Entity Type

Floor care

Coding

Coded - Design and coding required

Number of Pages Required

5+ page

Requirements
Must have
• Great pictures of different types of floors.

```html
<!DOCTYPE html>
<html lang="en">
<head>
<meta charset="utf-8">
<title>tilebaron – Commercial Floor Care</title>
<link href="https://fonts.googleapis.com/css2?family=Hanken+Grotesk:ital,wght@0,400;0,500;0,600;0,700;0,800;1,400&display=swap" rel="stylesheet">
<style>
:root{
  --green:#8cc63f;
  --ink:#111;
  --text:#2b2b2b;
  --muted:#6b6b6b;
  --page:#f1f1f1;
  --marble:#f7f7f4;
  --band:#ebebea;
  --black:#000;
  --white:#fff;
}
*{box-sizing:border-box;margin:0;padding:0}
html,body{width:1200px;height:4357px;overflow:hidden}
body{position:relative;background:var(--white);font-family:"Hanken Grotesk",Arial,sans-serif;color:var(--text)}
.abs{position:absolute}
.top-band{left:0;top:0;width:1200px;height:401px;background:var(--page)}
.brand-hero{left:0;top:70px;width:1200px;text-align:center;font-size:70px;font-weight:400;color:#1d1d1d;letter-spacing:1px}
.brand-hero .dot{display:inline-block;width:18px;height:18px;border-radius:50%;background:var(--green);margin-left:8px;vertical-align:middle}

.desktop{left:174px;top:225px;width:593px;height:2403px;background:var(--marble);overflow:hidden}
.mobile{left:804px;top:225px;width:218px;height:3950px;background:var(--marble);overflow:hidden}
.ph{position:absolute}
.wood{background:linear-gradient(160deg,#cfd1d3 0%,#9da2a6 40%,#8a5a36 70%,#b07a4b 100%)}
.hall{background:linear-gradient(180deg,#e9ebec 0%,#bfc3c6 45%,#7d7268 75%,#a89582 100%)}
.lounge{background:linear-gradient(160deg,#c9a968 0%,#6f6354 45%,#2f2f2f 65%,#9aa3a8 100%)}
.white-hall{background:linear-gradient(180deg,#e6e7e8 0%,#d6d8da 50%,#9a9da0 100%)}
.glass{background:linear-gradient(180deg,#c7dde9 0%,#8aa37a 45%,#a8b4bc 75%,#6e7780 100%)}
.lobby{background:linear-gradient(180deg,#f0ede6 0%,#c7b59a 50%,#d9d6d0 100%)}
.green-lobby{background:linear-gradient(120deg,#3d4a2b 0%,#b99a6a 35%,#6d5a45 60%,#a9a29a 100%)}

.label{font-size:9px;font-weight:600;color:var(--green)}
.h2{font-size:19px;line-height:1.3;font-weight:400;color:var(--ink)}
.rule{height:1px;background:#333}
.btn-dark{background:var(--black);color:var(--white);font-size:7px;font-weight:600;text-align:center}
.btn-green{background:var(--green);color:var(--white);font-size:7px;font-weight:600;text-align:center}
.para{font-size:5.5px;line-height:1.5;color:var(--muted)}

.nav a{font-size:6px;color:var(--ink);text-decoration:none;margin-left:14px}
.nav a.on{color:var(--green)}
.logo-sm{font-size:13px;color:var(--ink)}
.logo-sm .dot,.logo-ft .dot{display:inline-block;width:6px;height:6px;border-radius:50%;background:var(--green);margin-left:3px;vertical-align:middle}
.logo-ft{font-size:16px;color:var(--white)}

.svc{top:685px;height:185px;color:var(--white);font-size:7px;font-weight:600;text-align:center}
.svc span{position:absolute;bottom:14px;left:0;right:0}
.arrow-btn{width:14px;height:14px;border:1px solid #9a9a9a;border-radius:50%;background:rgba(255,255,255,.7)}
.sq-btn{width:16px;height:14px;background:rgba(255,255,255,.85)}

.field{background:var(--white);font-size:5px;color:#555;padding:2px 4px}
.ft-h{font-size:7px;color:var(--green);font-weight:600}
.ft-t{font-size:5px;color:#ddd;line-height:1.9}
.soc{width:12px;height:12px;border-radius:50%;background:#555}
.soc.on{background:var(--green)}

.m .label{font-size:8px}
.m .h2{font-size:17px;line-height:1.25}
.m .para{font-size:8.5px;line-height:1.55;color:#555}
.m .field{font-size:7px;padding:5px 8px}
.m .ft-h{font-size:9px}
.m .ft-t{font-size:7.5px;line-height:2.3}
.m .soc{width:17px;height:17px}
</style>
</head>
<body>

<div class="abs top-band"></div>
<div class="abs brand-hero">tilebaron<span class="dot"></span></div>

<!-- DESKTOP LAYOUT -->
<main class="abs desktop">
  <header class="abs" style="left:0;top:0;width:593px;height:37px">
    <div class="abs logo-sm" style="left:52px;top:12px">tilebaron<span class="dot"></span></div>
    <nav class="abs nav" style="left:300px;top:16px">
      <a class="on">Home</a><a>About</a><a>Services</a><a>Gallery</a><a>Contact</a>
    </nav>
    <div class="abs btn-dark" style="left:492px;top:13px;width:50px;height:14px;line-height:14px;font-size:6px">Get a Quote</div>
  </header>

  <section>
    <div class="ph hall" role="img" aria-label="Modern lobby with glossy marble floor and reception desk" style="left:202px;top:37px;width:391px;height:249px"></div>
    <div class="abs rule" style="left:0;top:131px;width:66px"></div>
    <h1 class="abs" style="left:100px;top:121px;width:300px;font-size:27px;line-height:1.05;font-weight:800;color:var(--ink)">LOVE YOUR FLOOR A<br>LITTLE MORE</h1>
    <div class="abs btn-green" style="left:100px;top:193px;width:61px;height:15px;line-height:15px;font-size:5.5px">Contact Us Today!</div>
    <div class="abs sq-btn" style="left:554px;top:268px"></div><div class="abs sq-btn" style="left:573px;top:268px"></div>
  </section>

  <section>
    <div class="ph wood" role="img" aria-label="Office corridor with elevators and polished wood floor" style="left:53px;top:286px;width:149px;height:262px"></div>
    <div class="abs label" style="left:254px;top:343px;font-size:6px">About us</div>
    <h2 class="abs h2" style="left:254px;top:355px;width:270px">A legacy of pursuing the highest standards of clean</h2>
    <p class="abs para" style="left:254px;top:419px;width:270px">It is a long established fact that a reader will be distracted by the readable content of a page when looking at its layout. The point of using lorem ipsum is that it has a more-or-less normal distribution of letters, as opposed to using 'content here, content here', making it look like readable english desktop publishing packages ...</p>
    <div class="abs btn-dark" style="left:254px;top:474px;width:62px;height:16px;line-height:16px;font-size:6px">Explore More</div>
  </section>

  <section>
    <div class="abs rule" style="left:0;top:617px;width:66px"></div>
    <div class="abs label" style="left:100px;top:596px;font-size:6px">Our Services</div>
    <h2 class="abs h2" style="left:100px;top:606px;width:300px">Commercial cleaning tailored to<br>your needs</h2>
    <div class="abs svc lounge" role="img" aria-label="Carpeted lounge with black chairs" style="left:0;width:149px"><span>CARPET SHAMPOOING</span></div>
    <div class="abs svc" role="img" aria-label="Blurred office hallway being burnished" style="left:149px;width:149px;background:linear-gradient(180deg,#8e8c86,#6b665e)">
      <div style="position:absolute;top:32px;left:0;right:0;font-size:9px">BURNISHING</div>
      <div style="position:absolute;top:47px;left:28px;right:28px;font-size:5px;font-weight:400;line-height:1.5">It is a long established fact that a reader will be distracted by the readable content of a page when looking at its layout.</div>
      <span style="font-size:5px;font-weight:400">Read More ↗</span>
    </div>
    <div class="abs svc wood" role="img" aria-label="Corridor with resurfaced wood floor" style="left:298px;width:149px"><span>RESURFACING</span></div>
    <div class="abs svc" role="img" aria-label="Curved glass walkway with plants" style="left:447px;width:146px;background:linear-gradient(180deg,#d2dbe0,#8d8a80 60%,#5d6b3e)"><span>POWER WASHING</span></div>
  </section>

  <section>
    <div class="abs rule" style="left:0;top:940px;width:66px"></div>
    <div class="abs label" style="left:100px;top:916px;font-size:6px">Projects Gallery</div>
    <h2 class="abs h2" style="left:100px;top:928px;width:200px">See the results of<br>our work.</h2>
    <div class="ph lounge" role="img" aria-label="Lounge with black chairs on patterned tile floor" style="left:12px;top:1048px;width:176px;height:199px"></div>
    <div class="ph white-hall" role="img" aria-label="White reception area with grey floor" style="left:202px;top:1004px;width:191px;height:137px"></div>
    <div class="ph glass" role="img" aria-label="Arched glass skybridge walkway" style="left:202px;top:1154px;width:191px;height:139px"></div>
    <div class="ph lobby" role="img" aria-label="Bright lobby with inlaid stone floor" style="left:405px;top:1048px;width:176px;height:199px"></div>
    <div class="abs btn-dark" style="left:268px;top:1313px;width:59px;height:15px;line-height:15px;font-size:5.5px">View All Work</div>
  </section>

  <section>
    <div class="abs" style="left:0;top:1378px;width:593px;height:245px;background:var(--band)"></div>
    <div class="abs rule" style="left:0;top:1438px;width:66px"></div>
    <div class="abs label" style="left:100px;top:1414px;font-size:6px">Testimonials</div>
    <h2 class="abs h2" style="left:100px;top:1426px">What our customers say</h2>
    <div class="ph lobby" role="img" aria-label="Client workplace interior" style="left:100px;top:1462px;width:88px;height:88px;border-radius:50%"></div>
    <div class="abs" style="left:100px;top:1565px;width:88px;text-align:center;font-size:6px;font-weight:600;color:var(--ink)">Standard chunk<br><span style="font-weight:400;font-size:5px">New York</span></div>
    <div class="abs" style="left:222px;top:1463px;font-size:18px;font-weight:800;color:var(--green)">”</div>
    <p class="abs" style="left:225px;top:1496px;width:268px;font-size:8px;font-style:italic;line-height:1.55;color:#444">“ It is a long established fact that a reader will be distracted by the readable content of a page when looking at its layout. The point of using lorem ipsum is that it has a more-or-less normal distribution readable english. ”</p>
    <div class="abs arrow-btn" style="left:220px;top:1565px;width:10px;height:10px"></div><div class="abs arrow-btn" style="left:236px;top:1565px;width:10px;height:10px"></div>
  </section>

  <section>
    <div class="abs rule" style="left:0;top:1684px;width:66px"></div>
    <div class="abs label" style="left:100px;top:1662px;font-size:6px">Latest News</div>
    <h2 class="abs h2" style="left:100px;top:1672px">Recent articles</h2>
    <div class="ph glass" role="img" aria-label="Open office with glass walls and wood floor" style="left:100px;top:1721px;width:394px;height:202px"></div>
    <div class="abs" style="left:303px;top:1809px;width:188px;height:107px;background:linear-gradient(90deg,rgba(140,140,150,.7),rgba(184,138,96,.85));padding:12px;color:var(--white)">
      <div style="font-size:9.5px;line-height:1.35">Lorem ipsum is simply dummy printing typesetting</div>
      <div style="font-size:5px;line-height:1.5;margin-top:8px">Lorem ipsum is simply dummy text of the printing and typesetting industry. Lorem ipsum has been the industry's...</div>
      <div style="font-size:5px;margin-top:6px">Read More ↗</div>
    </div>
    <div class="abs sq-btn" style="left:455px;top:1909px"></div><div class="abs sq-btn" style="left:475px;top:1909px"></div>
  </section>

  <section>
    <div class="ph green-lobby" role="img" aria-label="Hotel lobby with plants and marble reception desk" style="left:0;top:1970px;width:273px;height:267px"></div>
    <div class="abs" style="left:273px;top:1970px;width:320px;height:267px;background:linear-gradient(120deg,#9a8f83,#c7c3bd 50%,#b5aea6)"></div>
    <div class="abs" style="left:303px;top:2011px;font-size:5.5px;color:var(--white)">Get in touch</div>
    <h2 class="abs h2" style="left:303px;top:2035px;width:260px;color:var(--white)">Today is the perfect day<br>to get started.</h2>
    <div class="abs field" style="left:303px;top:2091px;width:118px;height:14px">Name</div>
    <div class="abs field" style="left:425px;top:2091px;width:118px;height:14px">Phone</div>
    <div class="abs field" style="left:303px;top:2116px;width:118px;height:14px">Email</div>
    <div class="abs field" style="left:425px;top:2116px;width:118px;height:14px">Services ⌄</div>
    <div class="abs field" style="left:303px;top:2141px;width:240px;height:28px">Message...</div>
    <div class="abs btn-dark" style="left:303px;top:2180px;width:56px;height:14px;line-height:14px;font-size:5.5px">Submit</div>
  </section>

  <footer class="abs" style="left:0;top:2237px;width:593px;height:166px;background:var(--black)">
    <div class="abs logo-ft" style="left:100px;top:45px">tilebaron<span class="dot"></span></div>
    <div class="abs ft-h" style="left:217px;top:44px">Contact Us</div>
    <div class="abs ft-t" style="left:217px;top:56px"><span style="color:var(--green)">☏</span> 1 (555) 018-2240<br><span style="color:var(--green)">✉</span> support@tilebaron.org<br><span style="color:var(--green)">⌖</span> 218 W Sample Ave, Suite 4,<br>&nbsp;&nbsp;TX 75001</div>
    <div class="abs ft-h" style="left:334px;top:44px">Company</div>
    <div class="abs ft-t" style="left:334px;top:56px">Home<br>About Us<br>Services<br>Gallery<br>Review</div>
    <div class="abs ft-t" style="left:389px;top:56px">Blog<br>Contact Us<br>Terms and Conditions<br>Privacy Policy</div>
    <div class="abs soc" style="left:480px;top:45px"></div>
    <div class="abs soc on" style="left:480px;top:63px"></div>
    <div class="abs soc" style="left:480px;top:81px"></div>
    <div class="abs soc" style="left:480px;top:99px"></div>
    <div class="abs" style="left:100px;top:131px;width:394px;height:1px;background:#333"></div>
    <div class="abs" style="left:100px;top:146px;width:394px;text-align:center;font-size:5px;color:#ccc">© 2024 <span style="color:var(--green)">Tile Baron</span>. All Rights Reserved</div>
  </footer>
</main>

<!-- MOBILE LAYOUT -->
<main class="abs mobile m">
  <header class="abs" style="left:0;top:0;width:218px;height:37px">
    <div class="abs logo-sm" style="left:10px;top:12px">tilebaron<span class="dot"></span></div>
    <svg class="abs" style="left:190px;top:14px" width="16" height="11" viewBox="0 0 16 11"><path d="M0 1h16M0 5.5h16M0 10h16" stroke="#111" stroke-width="1.6"/></svg>
  </header>
  <div class="ph hall" role="img" aria-label="Lobby with glossy marble floor" style="left:0;top:37px;width:218px;height:183px"></div>
  <h1 class="abs" style="left:0;top:86px;width:218px;text-align:center;font-size:15px;line-height:1.5;font-weight:800;color:var(--ink)">LOVE YOUR FLOOR A<br>LITTLE MORE</h1>
  <div class="abs btn-green" style="left:65px;top:140px;width:90px;height:15px;line-height:15px">Contact Us Today!</div>
  <div class="abs sq-btn" style="left:170px;top:201px"></div><div class="abs sq-btn" style="left:196px;top:201px"></div>

  <div class="abs rule" style="left:0;top:240px;width:24px"></div>
  <div class="abs label" style="left:10px;top:251px">About us</div>
  <h2 class="abs h2" style="left:10px;top:266px;width:200px">A legacy of pursuing the highest standards of clean</h2>
  <p class="abs para" style="left:10px;top:350px;width:200px">It is a long established fact that a reader will be distracted by the readable content of a lorem page when lookin at its layout. the point of using lorem ipsum is that it has a more-or-less normal distribution of letters, as opposed to using 'content here, content here', making it look like readable english desktop publishing packages ...</p>
  <div class="abs btn-dark" style="left:10px;top:503px;width:100px;height:23px;line-height:23px;font-size:8px">Explore More</div>
  <div class="ph wood" role="img" aria-label="Office corridor with wood floor" style="left:10px;top:547px;width:198px;height:159px"></div>

  <div class="abs rule" style="left:0;top:745px;width:24px"></div>
  <div class="abs label" style="left:10px;top:755px">Our Services</div>
  <h2 class="abs h2" style="left:10px;top:776px;width:200px">Commercial cleaning tailored to your needs</h2>
  <div class="ph lounge" role="img" aria-label="Carpeted lounge with black chairs" style="left:0;top:865px;width:218px;height:306px"></div>
  <div class="abs" style="left:0;top:1128px;width:218px;text-align:center;font-size:11px;font-weight:600;color:var(--white)">CARPET SHAMPOOING</div>
  <div class="abs" style="left:170px;top:845px;width:38px;height:38px;border-radius:50%;background:rgba(235,235,235,.9);font-size:7px;text-align:center;padding-top:12px;color:#222">DRAG<br>→</div>

  <div class="abs rule" style="left:0;top:1199px;width:24px"></div>
  <div class="abs label" style="left:10px;top:1205px">Projects Gallery</div>
  <h2 class="abs h2" style="left:10px;top:1222px;width:200px">See the results of<br>our work.</h2>
  <div class="ph lounge" role="img" aria-label="Lounge with black chairs on tile floor" style="left:10px;top:1276px;width:198px;height:225px"></div>
  <div class="ph white-hall" role="img" aria-label="White reception area" style="left:0;top:1513px;width:218px;height:157px"></div>
  <div class="ph glass" role="img" aria-label="Arched glass skybridge" style="left:0;top:1682px;width:218px;height:158px"></div>
  <div class="ph lobby" role="img" aria-label="Bright lobby with stone floor" style="left:10px;top:1852px;width:198px;height:225px"></div>

  <div class="abs" style="left:0;top:2097px;width:218px;height:437px;background:var(--band)"></div>
  <div class="abs rule" style="left:0;top:2120px;width:24px"></div>
  <div class="abs label" style="left:10px;top:2128px">Testimonials</div>
  <h2 class="abs h2" style="left:10px;top:2150px;width:200px">What our customers say</h2>
  <div class="ph lobby" role="img" aria-label="Client workplace interior" style="left:71px;top:2205px;width:76px;height:76px;border-radius:50%"></div>
  <div class="abs" style="left:0;top:2290px;width:218px;text-align:center;font-size:26px;font-weight:800;color:var(--green);line-height:1">”</div>
  <p class="abs" style="left:10px;top:2322px;width:198px;text-align:center;font-size:8.5px;font-style:italic;line-height:1.75;color:#444">“ It is a long established fact that a reader will be distracted by the readable content of a page when looking at its layout. the point of using lorem ipsum is that it has a more-or-less normal distribution readable english. ”</p>
  <div class="abs" style="left:0;top:2443px;width:218px;text-align:center;font-size:9.5px;font-weight:600;color:var(--ink)">Standard chunk</div>
  <div class="abs" style="left:0;top:2460px;width:218px;text-align:center;font-size:7px;color:#444">New York</div>
  <div class="abs arrow-btn" style="left:85px;top:2494px;border-color:var(--green)"></div><div class="abs arrow-btn" style="left:117px;top:2494px;border-color:var(--green)"></div>

  <div class="abs rule" style="left:0;top:2564px;width:24px"></div>
  <div class="abs label" style="left:10px;top:2567px">Latest News</div>
  <h2 class="abs h2" style="left:10px;top:2585px">Recent articles</h2>
  <div class="ph glass" role="img" aria-label="Open office with glass walls and plants" style="left:10px;top:2620px;width:198px;height:159px"></div>
  <div class="abs" style="left:10px;top:2779px;width:198px;height:150px;background:linear-gradient(90deg,#b9b0a6,#b88a62);padding:12px 18px;color:var(--white)">
    <div style="font-size:10px;line-height:1.4">Lorem ipsum is simply dummy printing typesetting</div>
    <div style="font-size:6.5px;line-height:1.6;margin-top:10px">Lorem ipsum is simply dummy text of the printing and typesetting industry lorem ipsum has been the industry's...</div>
    <div style="font-size:6.5px;margin-top:10px">Read More ↗</div>
  </div>
  <div class="abs sq-btn" style="left:160px;top:2911px;width:18px;height:18px"></div><div class="abs sq-btn" style="left:182px;top:2911px;width:18px;height:18px"></div>

  <div class="abs" style="left:0;top:2952px;width:218px;height:368px;background:linear-gradient(180deg,#9d958d,#d0cdc8 35%,#e2e1de)"></div>
  <div class="abs" style="left:0;top:2977px;width:218px;text-align:center;font-size:7px;color:var(--white)">Get in touch</div>
  <h2 class="abs h2" style="left:10px;top:2994px;width:198px;text-align:center;color:var(--white)">Today is the perfect day to get started.</h2>
  <div class="abs field" style="left:10px;top:3077px;width:198px;height:21px">Name</div>
  <div class="abs field" style="left:10px;top:3113px;width:198px;height:21px">Phone</div>
  <div class="abs field" style="left:10px;top:3149px;width:198px;height:21px">Email</div>
  <div class="abs field" style="left:10px;top:3185px;width:198px;height:21px">Services <span style="float:right">⌄</span></div>
  <div class="abs field" style="left:10px;top:3219px;width:198px;height:46px">Message...</div>
  <div class="abs btn-dark" style="left:65px;top:3281px;width:88px;height:20px;line-height:20px;font-size:8px">Submit</div>
  <div class="ph" role="img" aria-label="Glossy marble lobby floor with reflections" style="left:0;top:3320px;width:218px;height:219px;background:linear-gradient(180deg,#d6d2cc,#9a948c 55%,#6e6a64)"></div>

  <footer class="abs" style="left:0;top:3539px;width:218px;height:411px;background:var(--black)">
    <div class="abs logo-ft" style="left:0;top:40px;width:218px;text-align:center;font-size:21px">tilebaron<span class="dot"></span></div>
    <div class="abs ft-h" style="left:25px;top:90px">Contact Us</div>
    <div class="abs ft-t" style="left:25px;top:108px"><span style="color:var(--green)">☏</span> 1 (555) 018-2240<br><span style="color:var(--green)">✉</span> support@tilebaron.org<br><span style="color:var(--green)">⌖</span> 218 W Sample Ave, Suite 4,<br>&nbsp;&nbsp;&nbsp;TX 75001</div>
    <div class="abs ft-h" style="left:25px;top:197px">Company</div>
    <div class="abs ft-t" style="left:25px;top:216px">Home<br>About Us<br>Services<br>Gallery<br>Review</div>
    <div class="abs ft-t" style="left:103px;top:222px">Blog<br>Contact Us<br>Terms and Conditions<br>Privacy Policy</div>
    <div class="abs soc" style="left:55px;top:330px"></div>
    <div class="abs soc on" style="left:84px;top:330px"></div>
    <div class="abs soc" style="left:114px;top:330px"></div>
    <div class="abs soc" style="left:144px;top:330px"></div>
    <div class="abs" style="left:0;top:377px;width:218px;text-align:center;font-size:7px;color:#ccc">© 2024 <span style="color:var(--green)">Tile Baron</span>. All Rights Reserved</div>
  </footer>
</main>

</body>
</html>
```